Feng Shui Consultant needing a business card designed

please incorporate the following colours in the design: lilac (primarily)black and gold
Name of the business is: Harbour Feng Shui
The main design should incorporate a willow tree, to be the main focus of the design
The design should be modern and sophisticated
The back of the card should include the following details;
name; Marguerite Dolan
title: Accredited Feng Shui Consultant
phone number; 0457 392 815
email address; marguerite_dolan@quillmail.net
Specialising in Feng Shui and Space Clearing

Target Market(s)

Highend, affluent white collar clients. Well educated

Industry/Entity Type

Business

Colors
e3daeb

```html
<!DOCTYPE html>
<html lang="en">
<head>
<meta charset="utf-8">
<title>Harbour Feng Shui — Business Card</title>
<link rel="stylesheet" href="https://fonts.googleapis.com/css2?family=Questrial&display=swap">
<style>
  :root {
    --lilac: #e3daeb;
    --lilac-soft: #ebe5f0;
    --gold: #e6b915;
    --gold-deep: #c99a0a;
    --gold-pale: #ecdba6;
    --ink: #1a1a1a;
    --stage: #eeedf1;
    --foliage: #8fa877;
    --sky: #9cc3e6;
  }
  html, body {
    margin: 0;
    width: 1200px;
    height: 1200px;
    overflow: hidden;
    background: var(--stage);
    font-family: "Questrial", "Century Gothic", sans-serif;
  }
  .card {
    position: absolute;
    left: 198px;
    width: 808px;
    height: 493px;
    background: var(--lilac);
    box-shadow: 0 4px 14px rgba(0,0,0,0.25);
    overflow: hidden;
  }
  .card--front { top: 53px; }
  .card--back { top: 606px; }
  .card__art {
    position: absolute;
    inset: 0;
    width: 808px;
    height: 493px;
  }
  .brand {
    position: absolute;
    display: flex;
    align-items: center;
    color: var(--gold);
    white-space: nowrap;
  }
  .brand__dot {
    border-radius: 50%;
    background: var(--gold);
    flex: none;
  }
  .card--front .brand {
    left: 30px;
    top: 82px;
    font-size: 46px;
    gap: 16px;
  }
  .card--front .brand__dot { width: 34px; height: 34px; }
  .card--back .brand {
    left: 78px;
    top: 212px;
    font-size: 72px;
    gap: 24px;
  }
  .card--back .brand__dot { width: 54px; height: 54px; }
  .contact {
    position: absolute;
    left: 0;
    width: 500px;
    top: 212px;
    text-align: center;
    color: var(--ink);
  }
  .contact__name {
    margin: 0 0 6px;
    font-size: 42px;
    font-weight: 400;
    color: var(--gold);
    line-height: 1.1;
  }
  .contact__line {
    margin: 0;
    font-size: 21px;
    line-height: 27px;
  }
  .contact__title {
    display: flex;
    justify-content: center;
    align-items: center;
    gap: 10px;
  }
  .contact__rule {
    display: inline-block;
    width: 26px;
    height: 2px;
    background: var(--ink);
  }
</style>
</head>
<body>
  <section class="card card--front">
    <svg class="card__art" viewBox="0 0 808 493" aria-hidden="false">
      <defs>
        <linearGradient id="willow-scene" x1="0" y1="0" x2="0" y2="1">
          <stop offset="0" stop-color="var(--sky)"/>
          <stop offset="0.18" stop-color="#a9c095"/>
          <stop offset="0.7" stop-color="var(--foliage)"/>
          <stop offset="1" stop-color="#5f9a3c"/>
        </linearGradient>
      </defs>
      <rect x="440" y="0" width="368" height="493" fill="url(#willow-scene)" role="img" aria-label="Photograph of a weeping willow tree on a lawn under a blue sky"/>
      <path d="M0 0 H522 Q608 246 478 493 H0 Z" fill="var(--gold)"/>
      <path d="M0 0 H506 Q590 246 464 493 H0 Z" fill="var(--lilac)"/>
    </svg>
    <div class="brand"><span class="brand__dot"></span>Harbour Feng Shui</div>
    <div class="contact">
      <h1 class="contact__name">Marguerite Dolan</h1>
      <p class="contact__line contact__title"><span class="contact__rule"></span>Accredited Feng Shui Consultant<span class="contact__rule"></span></p>
      <p class="contact__line">0457 392 815</p>
      <p class="contact__line">marguerite_dolan@quillmail.net</p>
      <p class="contact__line">Specialising in Feng Shui and Space Clearing</p>
    </div>
  </section>

  <section class="card card--back">
    <svg class="card__art" viewBox="0 0 808 493" aria-hidden="true">
      <rect width="808" height="493" fill="var(--lilac)"/>
      <path d="M0 352 C170 336 300 340 400 380 C490 416 560 420 808 382 V493 H0 Z" fill="var(--gold-pale)"/>
      <path d="M0 372 C170 356 300 358 400 398 C490 434 560 436 808 402 V493 H0 Z" fill="var(--gold)"/>
    </svg>
    <div class="brand"><span class="brand__dot"></span>Harbour Feng Shui</div>
  </section>
</body>
</html>
```